Cleaning service website design

We need a new nice web design(logo will be the same) for a new cleaning service Company:

Informations about Company and logo you can take from flyers in attachments.

This is a cleaning service Company which have simple rules and we would like to show that(in checklist form) on website:

- What we do and that we're Cleaning Green

- Why us?

- How much(our pricing is simple)

Also we would like to communicate with clients by some nice/big pictures on website and the most important thing is our phone number and short/fast Freestimate.

Also there should be some space for description about our Company.

Generally all information on main page can be short: about us, about service(what we do), last reviews, tips (for example: Tip of the week) and other can be some introduction to subpage where will be more information.

There will be few subpages like: About us, About our service, Photos(Before and after), Reviews , Tips, FAQ, Contact, Looking for a Job? - most of them will be just text so you can project just one example.

```html
<!DOCTYPE html>
<html lang="en">
<head>
<meta charset="utf-8">
<title>Tidy Nest House Cleaning</title>
<link href="https://fonts.googleapis.com/css2?family=Open+Sans:wght@400;600;700&family=PT+Sans:wght@400;700&display=swap" rel="stylesheet">
<style>
:root{
  --blue:#0a52a8;
  --blue-dark:#063f86;
  --navy:#15408a;
  --green:#6cc164;
  --green-dark:#3f9a3c;
  --green-text:#5cb85c;
  --field:#e9fbe1;
  --orange:#f15a22;
  --ink:#333;
  --muted:#555;
  --pale-blue:#e3effa;
  --pale-grey:#f2f2f2;
  --white:#fff;
}
*{box-sizing:border-box;margin:0;padding:0}
html,body{width:783px;height:1200px;overflow:hidden;background:var(--white)}
body{position:relative;font-family:"Open Sans",Arial,sans-serif;color:var(--ink);font-size:8px;line-height:1.35}
.abs{position:absolute}
.head-font{font-family:"PT Sans",Arial,sans-serif}

.top-rule{left:0;top:0;width:783px;height:3px;background:var(--blue)}
.brand{left:80px;top:16px;width:104px;text-align:center}
.brand-name{display:flex;align-items:center;justify-content:center;gap:6px;font-family:"PT Sans",sans-serif;font-weight:700;font-size:20px;color:var(--green-dark)}
.brand-dot{width:12px;height:12px;border-radius:50%;background:var(--blue)}
.brand-sub{font-size:9px;color:var(--blue);margin-top:2px}

.social-top{left:290px;top:7px;display:flex;gap:12px;font-size:8.5px;color:#888}
.call-box{top:3px;height:20px;display:flex;font-family:"PT Sans",sans-serif;font-weight:700}
.call-box .label{background:var(--blue);color:#fff;font-size:11px;padding:2px 4px 0 8px}
.call-box .num{background:var(--green);color:#fff;font-size:14.5px;padding:0 5px;line-height:20px}
.call-top{left:565px}

.main-nav{left:280px;top:44px;display:flex;gap:24px;font-size:8px;color:#333;align-items:center}
.main-nav .current{background:var(--green);color:#fff;padding:3px 18px;clip-path:polygon(8% 0,100% 0,92% 100%,0 100%)}

.hero-photo{left:340px;top:62px;width:368px;height:248px;background:radial-gradient(ellipse at 60% 40%,#e6f2fb 0%,#cfe4f6 55%,#fff 100%)}
.welcome{left:80px;top:154px}
.welcome .pre{font-family:"PT Sans",sans-serif;font-size:17px;color:#222;line-height:1}
.welcome h1{font-family:"PT Sans",sans-serif;font-weight:700;font-size:22.5px;color:var(--navy);line-height:1.15}
.welcome p{width:255px;margin-top:5px;font-size:8px;color:#333}
.order-btn{left:80px;top:225px;width:152px;height:28px;background:linear-gradient(#f6743a,var(--orange));border-radius:3px;color:#fff;font-family:"PT Sans",sans-serif;font-weight:700;font-size:15px;text-align:center;line-height:28px;box-shadow:0 2px 2px rgba(0,0,0,.25)}

.green-band{left:0;top:310px;width:783px;height:306px;background:var(--green)}
.service{width:200px;display:flex;gap:7px}
.service-icon{flex:none;width:52px;height:52px;border-radius:50%;background:radial-gradient(circle,#5ab955 0,#3f9a3c 100%);border:2px solid #8fd48a}
.service h3{font-family:"PT Sans",sans-serif;font-size:11.5px;color:#1b4f1b;font-weight:700;line-height:1.05;margin-top:2px}
.service p{font-size:7px;color:#eaffea;margin-top:4px;width:125px;line-height:1.4}
.read-more{display:inline-block;margin-top:7px;background:#2f6b2d;color:#fff;font-size:7.5px;padding:2px 10px;clip-path:polygon(10% 0,100% 0,90% 100%,0 100%)}

.estimate{left:484px;top:300px;width:224px;height:316px}
.estimate-tab{position:absolute;left:0;top:0;width:224px;height:32px;background:linear-gradient(var(--blue),var(--blue-dark));color:#fff;font-family:"PT Sans",sans-serif;font-weight:700;font-size:17px;text-align:center;line-height:32px}
.estimate-tab span{color:var(--green);font-size:10px}
.estimate-body{position:absolute;left:6px;top:32px;width:212px;height:284px;background:#5db456;padding:3px 6px}
.field{height:19px;margin-top:3.2px;background:var(--field);border:1px solid #9ad792;font-size:7px;color:#7a8a7a;padding-left:8px;line-height:18px;position:relative}
.field.select::after{content:"\25B4\A\25BE";white-space:pre;position:absolute;right:6px;top:1px;font-size:6px;line-height:7px;color:#333}
.field.comments{height:58px;line-height:18px}
.submit{margin-top:5px;height:34px;background:linear-gradient(#1565bd,var(--blue-dark));color:#fff;font-family:"PT Sans",sans-serif;font-weight:700;font-size:17px;text-align:center;line-height:34px;border-radius:2px}

.about{left:80px;top:630px;width:332px;font-size:7.8px;color:var(--ink)}
.about h2{font-family:"PT Sans",sans-serif;font-weight:700;font-size:14px;color:var(--navy);line-height:1.05}
.about .tag{font-family:"PT Sans",sans-serif;font-size:14px;color:var(--blue);line-height:1.1}
.about p{margin-top:9px}
.checklist{list-style:none;margin-top:14px}
.checklist li{display:flex;align-items:center;gap:10px;font-weight:600;font-size:7.6px;height:15.8px}
.checklist svg{flex:none}

.testimonials{left:80px;top:1010px;width:336px}
.testimonials h2{font-family:"PT Sans",sans-serif;font-weight:700;font-size:14px;color:var(--navy)}
.arrows{position:absolute;right:4px;top:2px;display:flex;gap:4px}
.arrows span{width:12px;height:12px;border:1px solid #ccc;font-size:8px;color:#999;text-align:center;line-height:10px}
.quote{margin-top:6px;width:194px;background:#efefef;padding:7px 8px;font-size:7.8px;color:#444;height:52px;position:relative}
.quote::after{content:"";position:absolute;right:0;bottom:-12px;border-left:12px solid transparent;border-top:12px solid #ccc}
.author{position:absolute;left:204px;top:55px;display:flex;gap:6px;align-items:center}
.avatar{width:30px;height:30px;background:linear-gradient(#d8c8bc,#a89486)}
.author b{font-size:8px;display:block}
.author span{font-size:7.8px;color:#444}

.pricing{left:431px;top:616px;width:271px;height:224px;background:var(--pale-blue);padding:14px 12px;font-size:7.7px;color:#333}
.pricing h2{font-family:"PT Sans",sans-serif;font-weight:700;font-size:14px;color:var(--navy);padding-bottom:6px;border-bottom:1px solid #c8d9ea}
.price{margin-top:3px}
.price b{font-family:"PT Sans",sans-serif;font-size:14px;color:var(--green-text);font-weight:400}
.pricing .note{margin-top:3px}
.pricing .note em{font-style:normal;color:var(--blue)}
.pricing p{margin-top:8px}
.pricing .call b{font-family:"PT Sans",sans-serif;font-size:14px;color:var(--green-text);font-weight:400}

.tips{left:431px;top:840px;width:271px;height:235px;background:var(--pale-grey)}
.tips-head{position:absolute;left:0;top:0;width:150px;height:30px;background:var(--green);clip-path:polygon(0 0,100% 0,80% 100%,0 100%);color:#fff;font-family:"PT Sans",sans-serif;font-weight:700;font-size:14px;line-height:30px;padding-left:11px}
.tips-list{position:absolute;left:10px;top:40px;width:250px;font-size:7.6px;color:#333}
.tips-list p{text-decoration:underline;margin-bottom:10px;line-height:1.35}
.view-all{position:absolute;right:0;bottom:0;width:72px;height:16px;background:var(--blue);color:#fff;font-size:7.8px;text-align:right;padding-right:12px;line-height:16px;clip-path:polygon(18% 0,100% 0,100% 100%,0 100%)}

.footer{left:0;top:1117px;width:783px;height:83px;background:var(--blue)}
.footer-notch{left:385px;top:1117px;border-left:7px solid transparent;border-right:7px solid transparent;border-top:6px solid #fff}
.call-foot{left:565px;top:1122px}
.foot-nav{left:80px;top:1144px;display:flex;gap:12px;color:#fff;font-size:8px}
.foot-nav i{font-style:normal;opacity:.8}
.foot-social{left:588px;top:1159px;display:flex;gap:13px}
.foot-social span{width:12px;height:12px;border-radius:50%;background:#5b8fd0}
.foot-rule{left:80px;top:1182px;width:622px;height:1px;background:#2d6cbd}
.copyright{left:80px;top:1186px;font-size:7.8px;color:#a9c5ea}
</style>
</head>
<body>
<div class="abs top-rule"></div>

<div class="abs brand">
  <div class="brand-name"><span class="brand-dot"></span>Tidy Nest</div>
  <div class="brand-sub">house cleaning</div>
</div>

<div class="abs social-top"><span>Facenote</span><span>Chirper</span><span>Linkwork</span><span>CirclePlus</span><span>RSS Feeds</span></div>
<div class="abs call-box call-top"><span class="label">Call Us:</span><span class="num">555-014-2290</span></div>

<nav class="abs main-nav"><span class="current">Home</span><span>About Us</span><span>What We Do?</span><span>Why Us?</span><span>FAQ</span><span>Looking for a JOb?</span><span>Contact Us</span></nav>

<div class="abs hero-photo" role="img" aria-label="Three smiling cleaners in work overalls giving a thumbs up, holding cleaning supplies"></div>

<div class="abs welcome">
  <div class="pre">Welcome to</div>
  <h1>Tidy Nest House Cleaning</h1>
  <p>Lorem Ipsum. Proin gravida nibh vel velit auctor aliquet. Aenean sollicitudin, lorem quis bibendum auctor, nisi elit consequat ipsum.</p>
</div>
<div class="abs order-btn">ORDER NOW!</div>

<div class="abs green-band"></div>

<div class="abs service" style="left:80px;top:350px">
  <div class="service-icon"></div>
  <div><h3>Commercial Contract<br>Cleaning</h3><p>Lorem Ipsum. Proin gravida nibh vel velit auctor aliquet. Aenean sollicitudin, lorem quis bibendum auctor, nisi elit consequat ipsum.</p><span class="read-more">Read more</span></div>
</div>
<div class="abs service" style="left:299px;top:350px">
  <div class="service-icon"></div>
  <div><h3>Terminal Cleaning for<br>Medical Facilities</h3><p>Lorem Ipsum. Proin gravida nibh vel velit auctor aliquet. Aenean sollicitudin, lorem quis bibendum auctor, nisi elit consequat ipsum.</p><span class="read-more">Read more</span></div>
</div>
<div class="abs service" style="left:80px;top:488px">
  <div class="service-icon"></div>
  <div><h3>Construction Final<br>Cleans</h3><p>Lorem Ipsum. Proin gravida nibh vel velit auctor aliquet. Aenean sollicitudin, lorem quis bibendum auctor, nisi elit consequat ipsum.</p><span class="read-more">Read more</span></div>
</div>
<div class="abs service" style="left:299px;top:488px">
  <div class="service-icon"></div>
  <div><h3>Complete Floor<br>Services</h3><p>Lorem Ipsum. Proin gravida nibh vel velit auctor aliquet. Aenean sollicitudin, lorem quis bibendum auctor, nisi elit consequat ipsum.</p><span class="read-more">Read more</span></div>
</div>

<form class="abs estimate">
  <div class="estimate-tab">FREE ESTIMATE <span>&#9654;</span></div>
  <div class="estimate-body">
    <div class="field">FIRST &amp; LAST NAME:</div>
    <div class="field">ADDRESS:</div>
    <div class="field select">CITY:</div>
    <div class="field select">STATE/PROVINCE:</div>
    <div class="field">ZIP/POSTAL CODE:</div>
    <div class="field">PHONE:</div>
    <div class="field">EMAIL:</div>
    <div class="field select">HOW DID YOU HERE ABOUT US?</div>
    <div class="field comments">COMMENTS:</div>
    <div class="submit">SUBMIT</div>
  </div>
</form>

<section class="abs about">
  <h2>Brookvale Region House Cleaning Services</h2>
  <div class="tag">HOUSE CLEANING...TIDY NEST!</div>
  <p>We are Daniel and Marta Kowalczyk and we have personally experienced the struggle of finding a reliable and affordable maid service. We understand how busy life can be and cleaning is one of the tasks that falls off the list when you're stretched too thin. We are here to help! Let Tidy Nest take care of the house cleaning so you can focus on the more important things in life.</p>
  <p>Brookvale, Ashford, Linwood and Carver residents can count on us to make your home sparkle from top to bottom!</p>
  <p>When we clean your home, you can expect the following house cleaning tasks completed:</p>
  <ul class="checklist">
    <li><svg width="8" height="7" viewBox="0 0 8 7"><path d="M1 3.5 3 5.5 7 1" fill="none" stroke="#5cb85c" stroke-width="1.8"/></svg>Thoroughly clean your bathrooms, including toilet, sink, shower and tub</li>
    <li><svg width="8" height="7" viewBox="0 0 8 7"><path d="M1 3.5 3 5.5 7 1" fill="none" stroke="#5cb85c" stroke-width="1.8"/></svg>Carefully clean the kitchen, including the sink, countertops and outside of appliances</li>
    <li><svg width="8" height="7" viewBox="0 0 8 7"><path d="M1 3.5 3 5.5 7 1" fill="none" stroke="#5cb85c" stroke-width="1.8"/></svg>Tidy up around the house</li>
    <li><svg width="8" height="7" viewBox="0 0 8 7"><path d="M1 3.5 3 5.5 7 1" fill="none" stroke="#5cb85c" stroke-width="1.8"/></svg>Dusting of surfaces</li>
    <li><svg width="8" height="7" viewBox="0 0 8 7"><path d="M1 3.5 3 5.5 7 1" fill="none" stroke="#5cb85c" stroke-width="1.8"/></svg>Making mirrors shine</li>
    <li><svg width="8" height="7" viewBox="0 0 8 7"><path d="M1 3.5 3 5.5 7 1" fill="none" stroke="#5cb85c" stroke-width="1.8"/></svg>Make beds</li>
    <li><svg width="8" height="7" viewBox="0 0 8 7"><path d="M1 3.5 3 5.5 7 1" fill="none" stroke="#5cb85c" stroke-width="1.8"/></svg>Vacuuming rugs and carpeted areas</li>
    <li><svg width="8" height="7" viewBox="0 0 8 7"><path d="M1 3.5 3 5.5 7 1" fill="none" stroke="#5cb85c" stroke-width="1.8"/></svg>Cleaning of hardwood/tile/linoleum floors</li>
    <li><svg width="8" height="7" viewBox="0 0 8 7"><path d="M1 3.5 3 5.5 7 1" fill="none" stroke="#5cb85c" stroke-width="1.8"/></svg>Emptying garbage</li>
  </ul>
  <p>We take pride in our work and want to keep all of our customers happy. Let us know if you have special requests. If you are not satisfied with your house cleaning for any reason, please contact us and we will make it right. You can trust us to take care of your home as if it was our own.</p>
</section>

<section class="abs testimonials">
  <h2>Client TESTIMONIALS</h2>
  <div class="arrows"><span>&lsaquo;</span><span>&rsaquo;</span></div>
  <div class="quote">&ldquo; Donec nec justo eget felis facilisis fermentum. Aliquam porttitor mauris sit amet orci. Aenean dignissim pellentesque felis. &rdquo;</div>
  <div class="author"><div class="avatar" role="img" aria-label="Portrait of the reviewer"></div><div><b>Priya</b><span>Project manage</span></div></div>
</section>

<section class="abs pricing">
  <h2>Our maid service pricing is simple too:</h2>
  <div class="price" style="margin-top:6px"><b>$99</b> for homes 1,800-2,600 square feet*</div>
  <div class="price"><b>$89</b> for homes 1,000-1,800 square feet*</div>
  <div class="price"><b>$79</b> for homes less than 1,000 square feet*</div>
  <div class="note"><em>*rates are for bi-weekly service.</em> If your home is larger than 2,600 square feet, please call for a quote.</div>
  <p>It can take a little more time to get your home up to sparkling Tidy Nest standards so a small fee of $30 will be added the first time we come. After that, the regular visits will be at the value price seen above.</p>
  <p class="call"><b>CALL 555-014-2290</b> or fill out the form to the right to simplify your life!</p>
</section>

<section class="abs tips">
  <div class="tips-head">WEEKLY TIPS</div>
  <div class="tips-list">
    <p>Lorem Ipsum. Proin gravida nibh vel velit auctor aliquet. Aenean sollicitudin, lorem quis bibendum auctor.</p>
    <p>Nisi elit consequat ipsum, nec sagittis sem nibh id elit.</p>
    <p>Duis sed odio sit amet nibh vulputate cursus a sit amet mauris. Morbi accumsan ipsum velit. Nam nec tellus a odio tincidunt auctor.</p>
    <p>A ornare odio. Sed non mauris vitae erat consequat auctor eu in elit. Class aptent taciti sociosqu ad litora torquent per conubia nostra, per inceptos himenaeos. Mauris in erat justo.</p>
    <p>Nullam ac urna eu felis dapibus condimentum sit amet a augue. Sed non neque elit. Sed ut imperdiet nisi. Proin condimentum fermentum nunc. Etiam pharetra, erat sed fermentum feugiat.</p>
  </div>
  <div class="view-all">View All</div>
</section>

<footer class="abs footer"></footer>
<div class="abs footer-notch"></div>
<div class="abs call-box call-foot"><span class="label">Call Us:</span><span class="num">555-014-2290</span></div>
<nav class="abs foot-nav"><span>Home</span><i>|</i><span>About Us</span><i>|</i><span>What We Do?</span><i>|</i><span>Why Us?</span><i>|</i><span>FAQ</span><i>|</i><span>Looking for a JOb?</span><i>|</i><span>Contact Us</span></nav>
<div class="abs foot-social"><span></span><span></span><span></span><span></span><span></span></div>
<div class="abs foot-rule"></div>
<div class="abs copyright">&copy; 2013 Tidy Nest House Cleaning. All rights reserved.</div>
</body>
</html>
```